CRPG is needing business cards, and stationary created.

Pixel Forge created a logo for our business, and now we are wanting business cards, and stationary. I have included two designs of the same logo. Please feel free to use them as you want. The name of the company is Cedar Ridge Property Group LLC, the address is 812 NE Tamber Ln., Suite 9, the city & state is Fenwick Vale, Norland, zip code is 97815, Telephone number is 541-237-4190, Fax number is 541-237-8856, the name on the business card is Travis Lundqor CMCA

Industry/Entity Type

Property Management

Contact Information for Business Card

The card needs to look professional. Upscale.

Requirements
Must have
• The colors we are using are on the logo that has been uploaded.

```html
<!DOCTYPE html>
<html lang="en">
<head>
<meta charset="utf-8">
<title>Quillmont Property Group – Business Card</title>
<link rel="stylesheet" href="https://fonts.googleapis.com/css2?family=Exo+2:wght@600&family=Montserrat:wght@700&family=Open+Sans:wght@400&display=swap">
<style>
  :root {
    --teal: #178b76;
    --slate: #3b4450;
    --text: #2c2c2c;
    --stage: #e4e6e8;
    --card: #ffffff;
    --shape: #cfd4d7;
  }
  * { margin: 0; padding: 0; box-sizing: border-box; }
  html, body { width: 1200px; height: 450px; overflow: hidden; }
  body {
    background: var(--stage);
    position: relative;
    font-family: "Open Sans", sans-serif;
    color: var(--text);
  }
  .card {
    position: absolute;
    top: 65px;
    width: 519px;
    height: 297px;
    background: var(--card);
    overflow: hidden;
  }
  .card-front { left: 66px; }
  .card-back { left: 595px; }

  .seam-square {
    position: absolute;
    top: 20px;
    width: 260px;
    height: 260px;
    background: var(--shape);
  }
  .card-front .seam-square { left: 380px; }
  .card-back .seam-square { left: -140px; }

  .brand-small {
    position: absolute;
    left: 23px;
    top: 36px;
    display: flex;
    align-items: center;
    gap: 10px;
  }
  .brand-mark {
    width: 30px;
    height: 30px;
    background: var(--slate);
  }
  .brand-name-small {
    font-family: "Exo 2", sans-serif;
    font-weight: 600;
    font-size: 24px;
    line-height: 1;
    color: var(--teal);
    letter-spacing: 0.5px;
  }

  .person {
    position: absolute;
    left: 23px;
    top: 116px;
    font-family: "Montserrat", sans-serif;
    font-weight: 700;
  }
  .person-name { font-size: 17px; color: var(--slate); letter-spacing: 0.3px; }
  .person-title { font-size: 15px; color: var(--teal); margin-top: 2px; }

  .contact-list {
    position: absolute;
    left: 23px;
    top: 172px;
    list-style: none;
    font-size: 13px;
  }
  .contact-list li {
    display: flex;
    align-items: center;
    gap: 8px;
    height: 22px;
  }
  .contact-list svg { width: 13px; height: 13px; fill: var(--slate); }

  .address {
    position: absolute;
    left: 23px;
    top: 236px;
    font-size: 13px;
    line-height: 21px;
    font-style: normal;
  }

  .brand-large {
    position: absolute;
    left: 165px;
    top: 110px;
    width: 310px;
    text-align: center;
    font-family: "Exo 2", sans-serif;
    font-weight: 600;
    color: var(--teal);
  }
  .brand-large-name { font-size: 48px; line-height: 1; letter-spacing: 1px; }
  .brand-large-sub { font-size: 14px; letter-spacing: 4px; margin-top: 12px; }
</style>
</head>
<body>
  <section class="card card-front">
    <div class="seam-square"></div>
    <div class="brand-small">
      <span class="brand-mark"></span>
      <span class="brand-name-small">QUILLMONT</span>
    </div>
    <div class="person">
      <div class="person-name">TRAVIS LUNDQOR</div>
      <div class="person-title">CMCA</div>
    </div>
    <ul class="contact-list">
      <li>
        <svg viewBox="0 0 24 24" aria-hidden="true"><path d="M6.6 10.8a15.1 15.1 0 0 0 6.6 6.6l2.2-2.2a1 1 0 0 1 1-.25 11.4 11.4 0 0 0 3.6.57 1 1 0 0 1 1 1V20a1 1 0 0 1-1 1A17 17 0 0 1 3 4a1 1 0 0 1 1-1h3.5a1 1 0 0 1 1 1c0 1.250.2 2.45.57 3.57a1 1 0 0 1-.25 1z"/></svg>
        <span>555-237-4190</span>
      </li>
      <li>
        <svg viewBox="0 0 24 24" aria-hidden="true"><path d="M6 3h12v5H6zM3 9h18a1 1 0 0 1 1 1v7h-4v4H6v-4H2v-7a1 1 0 0 1 1-1zm5 7v3h8v-3z"/></svg>
        <span>555-237-8856</span>
      </li>
    </ul>
    <address class="address">
      812 NE Tamber Ln., Suite 9, the city &amp; state is Fenwick Vale<br>
      Norland, zip code is 97815
    </address>
  </section>

  <section class="card card-back">
    <div class="seam-square"></div>
    <div class="brand-large">
      <div class="brand-large-name">QUILLMONT</div>
      <div class="brand-large-sub">PROPERTY GROUP</div>
    </div>
  </section>
</body>
</html>
```